Vantrell Law Letterhead

We need a new letterhead design for a Law Firm. The address for the law firm is 4817 Larkspur Boulevard, Suite 250, Houston, Texas 77342. Phone Number: 832-619-3057; Fax Number: 832-407-1694. The logo is uploaded to the project.

```html
<!DOCTYPE html>
<html lang="en">
<head>
<meta charset="utf-8">
<title>Vantrell Law Letterhead</title>
<link href="https://fonts.googleapis.com/css2?family=Montserrat:wght@500;700&family=Hind:wght@400&family=Roboto:wght@400;500&display=swap" rel="stylesheet">
<style>
  :root {
    --navy: #1b2f5e;
    --red: #d71f26;
    --ink: #222222;
    --paper: #ffffff;
  }
  * { margin: 0; padding: 0; box-sizing: border-box; }
  html, body { width: 900px; height: 1200px; overflow: hidden; background: var(--paper); }
  .letterhead { position: relative; width: 900px; height: 1200px; background: var(--paper); overflow: hidden; color: var(--ink); }
  .abs { position: absolute; }
  .brand-top { left: 43px; top: 66px; font-family: "Montserrat", sans-serif; font-weight: 700; font-size: 30px; color: var(--navy); letter-spacing: .5px; }
  .date { right: 44px; top: 68px; font-family: "Montserrat", sans-serif; font-weight: 700; font-size: 14px; letter-spacing: .4px; }
  .to-label { left: 43px; top: 196px; font-family: "Montserrat", sans-serif; font-weight: 700; font-size: 15px; }
  .recipient { left: 43px; top: 224px; font-family: "Montserrat", sans-serif; font-weight: 500; font-size: 12.5px; line-height: 15.6px; }
  .salutation { left: 43px; top: 304px; font-family: "Montserrat", sans-serif; font-weight: 500; font-size: 12.5px; }
  .subject { left: 43px; top: 350px; font-family: "Montserrat", sans-serif; font-weight: 700; font-size: 15.5px; }
  .body-copy { left: 43px; top: 402px; width: 814px; font-family: "Hind", sans-serif; font-size: 13.4px; line-height: 17.2px; }
  .body-copy p + p { margin-top: 17px; }
  .closing { left: 43px; top: 716px; font-family: "Roboto", sans-serif; font-size: 12.5px; }
  .signature { left: 43px; top: 752px; width: 130px; height: 44px; background: linear-gradient(90deg, #e6e6e6, #f4f4f4); border-radius: 4px; }
  .signer { left: 43px; top: 815px; font-family: "Roboto", sans-serif; font-size: 12.5px; line-height: 17px; }
  .signer .role { font-weight: 500; }
  .tab { left: 0; top: 951px; width: 40px; height: 37px; background: var(--navy); border-radius: 0 19px 19px 0; }
  .contact { font-family: "Roboto", sans-serif; font-size: 12.5px; }
  .contact-row { left: 62px; display: flex; align-items: center; gap: 12px; }
  .contact-row svg { width: 16px; height: 16px; }
  .phone { top: 954px; }
  .fax { top: 987px; }
  .address { left: 236px; top: 952px; line-height: 17.2px; }
  .brand-foot { left: 55px; top: 1066px; display: flex; align-items: center; gap: 16px; font-family: "Montserrat", sans-serif; font-weight: 700; font-size: 42px; color: var(--navy); }
  .brand-foot .mark { width: 34px; height: 34px; background: var(--red); }
  .corner-disc { left: 664px; top: 923px; width: 280px; height: 280px; border-radius: 50%; background: var(--navy); }
</style>
</head>
<body>
<div class="letterhead">
  <div class="abs brand-top">Vantrell Law</div>
  <div class="abs date">JANUARY 22, 2022</div>

  <div class="abs to-label">TO</div>
  <div class="abs recipient">FINANCE MANAGER,<br>Address<br>Recipient<br>Tel: 8320000000</div>
  <div class="abs salutation">Dear Mr. Ellison Grant</div>
  <div class="abs subject">RE: LETTERHEAD REFERENCE</div>

  <div class="abs body-copy">
    <p>Lorem ipsum dolor sit amet, consectetuer adipiscing elit, sed diam nonummy nibh euismod tincidunt ut laoreet dolore magna aliquam erat volutpat. Ut wisi enim ad minim veniam, quis nostrud exerci tation ullamcorper suscipit lobortis nisl ut aliquip ex ea commodo consequat. Duis autem vel eum iriure dolor in hendrerit in vulputate velit esse molestie consequat, vel illum dolore eu feugiat nulla facilisis at vero eros et accumsan et iusto odio dignissim qui blandit praesent luptatum zzril delenit augue duis dolore te feugait nulla facilisi.</p>
    <p>Lorem ipsum dolor sit amet, cons ectetuer adipiscing elit, sed diam nonummy nibh euismod tincidunt ut laoreet dolore magna aliquam erat volutpat. Ut wisi enim ad minim veniam, quis nostrud exerci tation ullamcorper suscipit lobortis nisl ut aliquip ex ea commodo consequat.</p>
    <p>Lorem ipsum dolor sit amet, consectetuer adipiscing elit, sed diam nonummy nibh euismod tincidunt ut laoreet dolore magna aliquam erat volutpat. Ut wisi enim ad minim veniam, quis nostrud exerci tation ullamcorper suscipit lobortis nisl ut aliquip ex ea commodo consequat. Duis autem vel eum iriure dolor in hendrerit in vulputate velit esse molestie consequat, vel illum dolore eu feugiat nulla facilisis at vero eros et accumsan et iusto odio dignissim qui blandit praesent luptatum zzril delenit augue duis dolore te feugait nulla facilisi.</p>
  </div>

  <div class="abs closing">Sincerely,</div>
  <div class="abs signature" role="img" aria-label="Handwritten signature of the branch manager"></div>
  <div class="abs signer">Marcus Talbot<br><span class="role">Branch Manager</span></div>

  <div class="abs tab"></div>
  <div class="abs contact contact-row phone">
    <svg viewBox="0 0 16 16" aria-hidden="true"><rect width="16" height="16" rx="3" fill="#d71f26"/><path d="M5 3.5l1.6 2.3-1 1c.6 1.3 1.5 2.2 2.7 2.8l1-1 2.3 1.5-.7 1.9c-3.6-.3-6.5-3.2-6.8-6.8z" fill="#fff"/></svg>
    <span>832-619-3057</span>
  </div>
  <div class="abs contact contact-row fax">
    <svg viewBox="0 0 16 16" aria-hidden="true"><rect x="4" y="1" width="8" height="5" fill="none" stroke="#d71f26" stroke-width="1.5"/><rect x="1" y="5.5" width="14" height="6" rx="1.5" fill="#d71f26"/><rect x="4" y="9.5" width="8" height="5.5" fill="#fff" stroke="#d71f26" stroke-width="1.5"/></svg>
    <span>832-407-1694</span>
  </div>
  <div class="abs contact address">4817 Larkspur Boulevard,<br>Suite 250, Houston<br>Texas 77342</div>

  <div class="abs brand-foot"><span class="mark"></span>Vantrell Law</div>

  <div class="abs corner-disc"></div>
</div>
</body>
</html>
```